Pharmacy/medical flyer for special supplement for cardio-vascular health

We need a 3-fold flyer for a special supplement for cardio-vascular health.<br/>We are a company dealing with health and helping people to get back their health via natural ingredients.<br/>In our portfolio we have a special 100% natural supplement VORELUNA Cardio, which supports maintaining blood pressure in normal range, promote healthy hearth and vessels, supports lowering of bad cholesterol and contribute to higher quality of life.<br/>We would like to see designs that use color black and silver similar to design of our supplement label (photo in attachment), so that the whole design looks very luxury. <br/>We are open also to another color designs like in green for example, if it will look luxury.<br/>The final design should communicate healthy and happy couple aged 40-60 years and top quality supplement supplied with trademark ingredients backed by science and research.<br/>On the flyer there should be section with benefits of the product,<br/>section with ingredients list and composition of supplement with the logos of trademarked ingredients ( will supply photos on demand), section with some testimonials ( 3 testimonial we provide with photos ) + another 2 testimonials without the photo, section deditacated to research and clinicial trials of some ingredients, section with our company contact information.<br/>In attachement we enclose our company logo, product photo (can supply in PSD on demand), <br/><br/>Thank your for your designs<br/>Regards,<br/>Teodor Vasquil<br/>VORELUNA
Health and wellness, People 40+
Health Product

```html
<!DOCTYPE html>
<html lang="en">
<head>
<meta charset="utf-8">
<title>VORELUNA Cardio – Trifold Flyer</title>
<link rel="stylesheet" href="https://fonts.googleapis.com/css2?family=Montserrat:wght@400;500;600;700&display=swap">
<style>
:root{
  --board:#444444;
  --green:#5c9b30;
  --green-dark:#4b8a26;
  --green-deep:#1f5e3f;
  --teal:#1c7a58;
  --ink:#2b2b2b;
  --muted:#3d3d3d;
  --white:#ffffff;
  --wash:#eef1ea;
}
*{box-sizing:border-box;margin:0;padding:0}
html,body{width:857px;height:1200px;overflow:hidden;background:var(--board)}
body{font-family:"Montserrat",Arial,sans-serif;color:var(--ink)}
.board{position:relative;width:857px;height:1200px;background:var(--board)}
.sheet{position:absolute;left:87px;width:672px;height:475px;background:var(--white);overflow:hidden;box-shadow:0 2px 6px rgba(0,0,0,.35)}
.sheet--front{top:92px}
.sheet--middle{top:646px}
.board-label{position:absolute;left:0;width:857px;text-align:center;color:var(--white);font-weight:500;font-size:25px;letter-spacing:1px}
.board-label--front{top:584px}
.board-label--middle{top:1138px}
.panel{position:absolute;top:0;width:224px;height:475px;overflow:hidden}
.panel--1{left:0}.panel--2{left:224px}.panel--3{left:448px}
.abs{position:absolute}
.center{text-align:center}
.copy{text-align:justify;text-align-last:center;hyphens:auto}
.brand-name{font-weight:400;letter-spacing:2px;color:var(--green)}
.heartbeat{display:block;margin:0 auto}
.photo{position:absolute}

/* front */
.front-sun{left:0;top:0;width:224px;height:475px;background:radial-gradient(circle at 30% 45%,#ffb300 0%,#ff9a1f 28%,#f7d77a 55%,#f7efd6 80%,#fbf6ea 100%)}
.about-title{left:0;top:76px;width:224px;font-size:16px;font-weight:500;color:var(--ink)}
.about-title span{color:var(--green)}
.about-copy{left:29px;top:134px;width:168px;font-size:10.2px;line-height:13.4px;color:var(--ink)}
.couple-photo{left:-30px;top:330px;width:300px;height:300px;border-radius:50%;border:6px solid var(--green);background:linear-gradient(160deg,#6f8a55 0%,#a9b79a 40%,#d8d2c4 70%,#3c3f3a 100%)}
.contact-panel{background:var(--green);color:var(--white)}
.contact-name{left:0;top:128px;width:224px;font-size:14px;color:var(--white);letter-spacing:2px}
.contact-copy{left:22px;top:196px;width:180px;font-size:8.6px;line-height:11.6px}
.contact-item{left:0;width:224px;font-size:8.2px;font-weight:500;letter-spacing:.3px}
.contact-icon{position:absolute;left:103px}
.social{position:absolute;top:430px;width:15px;height:15px;border:1.2px solid var(--white);border-radius:50%}
.cover-name{left:32px;top:28px;width:160px;font-size:19px;text-align:center}
.cover-title{left:10px;top:381px;width:210px;font-size:24px;line-height:26px;font-weight:500;color:var(--green-deep);text-align:center}
.cover-web{left:0;top:446px;width:224px;font-size:10px;font-weight:700;color:var(--green-deep)}

/* middle */
.mid-title{left:20px;top:28px;width:184px;font-size:9.6px;line-height:12.2px;font-weight:500;color:var(--green)}
.mid-copy{left:18px;width:190px;font-size:8.7px;line-height:11px;color:var(--muted)}
.food-photo{left:40px;top:336px;width:150px;height:84px;border-radius:42px;background:radial-gradient(circle at 45% 55%,#e0b36a 0%,#c0522e 35%,#7a8d3a 60%,#f2f2ef 85%)}
.panel-web{left:0;top:450px;width:224px;font-size:8.6px;font-weight:600;color:var(--white)}
.why-panel{background:linear-gradient(180deg,#5e9d33 0%,#63a238 50%,#5a9a2f 100%)}
.why-title{left:14px;top:29px;width:196px;font-size:9.6px;line-height:12.2px;font-weight:500;color:var(--white)}
.why-copy{left:18px;width:188px;font-size:8.7px;line-height:11px;color:var(--white)}
.divider{left:40px;width:144px;height:2px;background:linear-gradient(90deg,transparent,rgba(255,255,255,.9),transparent)}
.cardio-title{left:0;top:27px;width:224px;font-size:13px;font-weight:500;color:var(--ink)}
.cardio-title span{color:var(--green)}
.cardio-copy{left:17px;top:84px;width:192px;font-size:8.6px;line-height:11px;color:var(--muted)}
.benefits{left:17px;top:155px;width:196px;list-style:none;font-size:8px;line-height:10.5px;color:var(--ink)}
.benefits li{position:relative;padding-left:16px;margin-bottom:4px}
.benefits svg{position:absolute;left:0;top:1px}
.table-photo{left:-22px;top:254px;width:400px;height:400px;border-radius:50%;border:5px solid var(--green);background:linear-gradient(150deg,#e7eef0 0%,#dde8ea 45%,#cfdfe3 70%,#c9d9d0 100%)}
.product-name{left:40px;top:363px;width:160px;font-size:15px;text-align:center}
.product-web{left:0;top:450px;width:224px;font-size:8.6px;font-weight:600;color:var(--green-deep)}
</style>
</head>
<body>
<div class="board">

  <!-- FRONT SHEET -->
  <section class="sheet sheet--front">
    <div class="panel panel--1">
      <div class="abs about-title center">ABOUT <span>US:</span></div>
      <svg class="abs heartbeat" style="left:82px;top:98px" width="62" height="24" viewBox="0 0 62 24" aria-hidden="true">
        <path d="M0 13 H12 L16 18 L22 2 L27 22 L31 8 L34 13 H42" fill="none" stroke="var(--teal)" stroke-width="2"/>
        <path d="M45 13 H50 M53 13 H58" fill="none" stroke="var(--teal)" stroke-width="2"/>
      </svg>
      <p class="abs about-copy copy">The name Voreluna is inspired by the Greek goddess of health and well-being (Panacea). The current hectic period of unhealthy lifestyles and civilization diseases brought us to this philosophy. We ourselves have found ourselves on the brink of life burnout, even though we have cared for our whole lives and minds. Unfortunately, in a world full of stress, lack of exercise and junk food, this is not enough. More needs to be done.</p>
      <div class="photo couple-photo" role="img" aria-label="Photo of a smiling senior couple jogging outdoors in a park"></div>
    </div>

    <div class="panel panel--2 contact-panel">
      <div class="abs contact-name center">VORELUNA</div>
      <p class="abs contact-copy copy">If you have any questions about our products or your health, feel free to contact us. We will be happy to provide you with a free consultation and answer any questions that will help you restore your health and life. We are looking forward to you</p>
      <svg class="contact-icon" style="top:289px" width="18" height="18" viewBox="0 0 18 18" aria-hidden="true">
        <circle cx="9" cy="9" r="8" fill="none" stroke="#fff" stroke-width="1.2"/>
        <path d="M6 5 L7.5 5 L8.3 7 L7.3 8 C7.8 9.2 8.8 10.2 10 10.7 L11 9.7 L13 10.5 L13 12 C10 12.6 5.4 8 6 5 Z" fill="#fff"/>
      </svg>
      <div class="abs contact-item center" style="top:311px">+421 900 555 018</div>
      <svg class="contact-icon" style="top:339px;left:104px" width="17" height="11" viewBox="0 0 17 11" aria-hidden="true">
        <rect x=".6" y=".6" width="15.8" height="9.8" fill="none" stroke="#fff" stroke-width="1.2"/>
        <path d="M.6 .6 L8.5 6.5 L16.4 .6" fill="none" stroke="#fff" stroke-width="1.2"/>
      </svg>
      <div class="abs contact-item center" style="top:352px">INFO@VORELUNA.SK</div>
      <svg class="contact-icon" style="top:378px" width="18" height="18" viewBox="0 0 18 18" aria-hidden="true">
        <g fill="none" stroke="#fff" stroke-width="1.2">
          <circle cx="9" cy="9" r="8"/><ellipse cx="9" cy="9" rx="3.6" ry="8"/>
          <path d="M1 9 H17 M2.5 5 H15.5 M2.5 13 H15.5 M9 1 V17"/>
        </g>
      </svg>
      <div class="abs contact-item center" style="top:401px">WWW.VORELUNA.SK</div>
      <span class="social" style="left:80px"></span>
      <span class="social" style="left:104px"></span>
      <span class="social" style="left:128px"></span>
    </div>

    <div class="panel panel--3">
      <div class="photo front-sun" role="img" aria-label="Photo of a woman with arms spread wide enjoying warm golden sunlight"></div>
      <div class="abs cover-title">ENERGY &amp;<br>HAPPINESS</div>
      <div class="abs cover-web center">WWW.VORELUNA.SK</div>
    </div>

    <svg class="abs" style="left:0;top:0" width="672" height="130" viewBox="0 0 672 130" aria-hidden="true">
      <defs>
        <linearGradient id="topWash" x1="0" x2="1" y1="0" y2="0">
          <stop offset="0" stop-color="#e9eee2"/><stop offset=".62" stop-color="#f3f5f0"/><stop offset=".7" stop-color="#ffffff"/><stop offset="1" stop-color="#ffffff"/>
        </linearGradient>
      </defs>
      <path d="M0 0 H672 V66 C620 86 540 108 448 104 C390 100 330 56 240 48 C160 42 80 58 0 80 Z" fill="url(#topWash)"/>
      <path d="M0 80 C80 58 160 42 240 48 C330 56 390 100 448 104 C540 108 620 86 672 66" fill="none" stroke="var(--green)" stroke-width="7"/>
    </svg>
    <div class="abs brand-name cover-name" style="left:480px">VORELUNA</div>
  </section>
  <div class="board-label board-label--front">FRONT PAGE</div>

  <!-- MIDDLE SHEET -->
  <section class="sheet sheet--middle">
    <div class="panel panel--1">
      <h2 class="abs mid-title center">CONNECTION OF CHINESE MEDICINE AND MOLECULAR SCIENCE</h2>
      <p class="abs mid-copy copy" style="top:83px">At Voreluna, we combine the latest knowledge of molecular science at the cellular level with the centuries-old Chinese ancient art of life and health - Wujijuan. By combining these two philosophies, we bring you the best of both worlds in the purest form that nature itself offers us.</p>
      <p class="abs mid-copy copy" style="top:179px">On the one hand, they are natural vitamins, minerals and extracts of exceptional plants used for centuries for their beneficial effects. They support your long-term health, vitality, nutrition or body regeneration at the cellular level. All in a concentrated form of nutritional supplement.</p>
      <p class="abs mid-copy copy" style="top:274px">On the other hand, they are simple practices that will heal your body and mind and restore you with the vital energy that we are unfortunately losing due to modern lifestyles.</p>
      <div class="photo food-photo" role="img" aria-label="Photo of a healthy plate of vegetables, bread and grains with a glass of water"></div>
    </div>

    <div class="panel panel--2 why-panel">
      <h2 class="abs why-title center">WHY VORELUNA IS THE KEY TO YOUR HEALTH</h2>
      <svg class="abs heartbeat" style="left:81px;top:60px" width="62" height="24" viewBox="0 0 62 24" aria-hidden="true">
        <path d="M0 13 H12 L16 18 L22 2 L27 22 L31 8 L34 13 H42" fill="none" stroke="#fff" stroke-width="2"/>
        <path d="M45 13 H50 M53 13 H58" fill="none" stroke="#fff" stroke-width="2"/>
      </svg>
      <p class="abs why-copy copy" style="top:91px">The name Voreluna is inspired by the Greek goddess of health and well-being (Panacea). The current hectic period of unhealthy lifestyles and civilization diseases brought us to this philosophy.</p>
      <div class="abs divider" style="top:156px"></div>
      <p class="abs why-copy copy" style="top:174px">We ourselves have found ourselves on the brink of life burnout, even though we have cared for our whole lives and minds. Unfortunately, in a world full of stress, lack of exercise and junk food, this is not enough. More needs to be done.</p>
      <div class="abs divider" style="top:250px"></div>
      <p class="abs why-copy copy" style="top:271px">But how to do it when it is at work from morning to evening, is exhausted, does not manage to exercise or eat healthy, and can only find energy for your family or partner. That is why we come up with a solution for people living in a Western way of life that is no longer sustainable. You ask how?</p>
    </div>

    <svg class="abs" style="left:0;top:340px" width="448" height="135" viewBox="0 0 448 135" aria-hidden="true">
      <path d="M0 40 C90 80 200 88 300 60 C360 44 410 28 448 22 V135 H0 Z" fill="var(--green-dark)"/>
      <path d="M0 48 C90 88 200 96 300 68 C360 52 410 36 448 30" fill="none" stroke="#ffffff" stroke-width="3"/>
    </svg>
    <div class="abs panel-web center" style="left:0">WWW.VORELUNA.SK</div>
    <div class="abs panel-web center" style="left:224px">WWW.VORELUNA.SK</div>

    <div class="panel panel--3">
      <h2 class="abs cardio-title center">VORELUNA <span>CARDIO</span></h2>
      <svg class="abs heartbeat" style="left:81px;top:52px" width="62" height="24" viewBox="0 0 62 24" aria-hidden="true">
        <path d="M0 13 H12 L16 18 L22 2 L27 22 L31 8 L34 13 H42" fill="none" stroke="var(--teal)" stroke-width="2"/>
        <path d="M45 13 H50 M53 13 H58" fill="none" stroke="var(--teal)" stroke-width="2"/>
      </svg>
      <p class="abs cardio-copy copy">Exceptional combination of superfoods like black garlic, extracts of medicinal mushrooms reishi and maitake, acerola cherry and natural magnesium from the sea. Developed to support your heart, blood vessels and immune system.</p>
      <ul class="abs benefits">
        <li><svg width="10" height="10" viewBox="0 0 10 10" aria-hidden="true"><circle cx="5" cy="5" r="4.3" fill="none" stroke="var(--green)" stroke-width="1"/><path d="M2.8 5 L4.4 6.6 L7.4 3.4" fill="none" stroke="var(--green)" stroke-width="1.1"/></svg>Helps keep blood pressure at normal levels</li>
        <li><svg width="10" height="10" viewBox="0 0 10 10" aria-hidden="true"><circle cx="5" cy="5" r="4.3" fill="none" stroke="var(--green)" stroke-width="1"/><path d="M2.8 5 L4.4 6.6 L7.4 3.4" fill="none" stroke="var(--green)" stroke-width="1.1"/></svg>Strengthens the immune system</li>
        <li><svg width="10" height="10" viewBox="0 0 10 10" aria-hidden="true"><circle cx="5" cy="5" r="4.3" fill="none" stroke="var(--green)" stroke-width="1"/><path d="M2.8 5 L4.4 6.6 L7.4 3.4" fill="none" stroke="var(--green)" stroke-width="1.1"/></svg>It improves cardiovascular health</li>
        <li><svg width="10" height="10" viewBox="0 0 10 10" aria-hidden="true"><circle cx="5" cy="5" r="4.3" fill="none" stroke="var(--green)" stroke-width="1"/><path d="M2.8 5 L4.4 6.6 L7.4 3.4" fill="none" stroke="var(--green)" stroke-width="1.1"/></svg>Reduces inflammation in the body and oxidative stress in cells caused by aging</li>
      </ul>
      <div class="photo table-photo" role="img" aria-label="Photo of fresh herbs, limes, chopped vegetables and a salad bowl on a pale table"></div>
      <div class="abs brand-name product-name">VORELUNA</div>
      <div class="abs product-web center">WWW.VORELUNA.SK</div>
    </div>
  </section>
  <div class="board-label board-label--middle">MIDDLE PAGE</div>

</div>
</body>
</html>
```